New Zealand Marlborough Sauvignon Blanc wine packaging design

We need packaging design for our new wine brand, Dunmore Hale. The wine is a New Zealand Marlborough Sauvignon Blanc. We would like the packaging will portray elegance and style with an understated label. We are looking for a label that portrays the elegance of the French Riviera. The label should be round or pill shaped.
Updates

Industry/Entity Type

Wine

Font styles to use
Serif
Sans Serif

Requirements
Must have
• The words in order of importance: Dunmore Hale, Sauvignon Blanc, Marlborough, New Zealand. It should be fit to the bottle posted in the links
Nice to have
• a pill shape or circular shape
Should not have
• Illustrations of wine bottles, wine glasses, or grapes

```html
<!DOCTYPE html>
<html lang="en">
<head>
<meta charset="utf-8">
<title>Dunmore Hale Sauvignon Blanc Label</title>
<link href="https://fonts.googleapis.com/css2?family=Allura&family=Oswald:wght@300&family=Cinzel:wght@400&family=Libre+Baskerville:wght@700&display=swap" rel="stylesheet">
<style>
  :root {
    --backdrop: #f3f2ee;
    --label-white: #ffffff;
    --ink: #1f1f1f;
    --wine-red: #4a1414;
    --bird-taupe: #74695a;
  }
  html, body {
    margin: 0;
    padding: 0;
    width: 1200px;
    height: 1200px;
    overflow: hidden;
    background: var(--backdrop);
  }
  .canvas {
    position: relative;
    width: 1200px;
    height: 1200px;
  }
  .label {
    position: absolute;
    left: 207px;
    top: 207px;
    width: 786px;
    height: 786px;
    border-radius: 50%;
    background: var(--label-white);
    overflow: hidden;
  }
  .label > * {
    position: absolute;
  }
  .emblem {
    left: 315px;
    top: 101px;
    width: 141px;
    height: 112px;
    display: block;
  }
  .divider {
    left: 297px;
    top: 254px;
    width: 189px;
    height: 2px;
    background: var(--wine-red);
  }
  .brand-name {
    left: 0;
    right: 0;
    top: 270px;
    margin: 0;
    text-align: center;
    font-family: "Allura", cursive;
    font-weight: 400;
    font-size: 132px;
    line-height: 150px;
    color: var(--ink);
  }
  .varietal {
    left: 0;
    right: 0;
    top: 443px;
    text-align: center;
    font-family: "Oswald", sans-serif;
    font-weight: 300;
    font-size: 42px;
    line-height: 56px;
    letter-spacing: 0.22em;
    padding-left: 0.22em;
    color: var(--ink);
  }
  .region-band {
    left: 0;
    right: 0;
    top: 543px;
    height: 99px;
    background: var(--wine-red);
    display: flex;
    align-items: center;
    justify-content: center;
    font-family: "Cinzel", serif;
    font-size: 44px;
    letter-spacing: 0.02em;
    color: var(--label-white);
  }
  .country {
    left: 0;
    right: 0;
    top: 676px;
    text-align: center;
    font-family: "Libre Baskerville", serif;
    font-weight: 700;
    font-size: 30px;
    line-height: 34px;
    color: var(--ink);
  }
</style>
</head>
<body>
  <main class="canvas">
    <section class="label">
      <svg class="emblem" viewBox="0 0 141 112" role="img" aria-label="Kiwi bird silhouette emblem">
        <rect width="141" height="112" rx="10" fill="var(--bird-taupe)"/>
      </svg>
      <div class="divider"></div>
      <h1 class="brand-name">Dunmore Hale</h1>
      <div class="varietal">SAUVIGNON BLANC</div>
      <div class="region-band">Marlborough</div>
      <div class="country">NEW ZEALAND</div>
    </section>
  </main>
</body>
</html>
```